Create a pouch design for a new sports supplement product

Dimensions are 235mm (width) x 335mm (length) x 110mm (gusset)
File 1 - Extension of design brief please read both briefs
File 2 - Is 2 potential pouches this is just to give you a better example of size the dimensions are for the pouch on the right. This picture is not to give you design ideas as I am not very keen on either of these designs.
We need a design to be printed onto the pouches of our whey protein product. The brand name is 'Stellar Fuelworks' and needs to be displayed on the packaging either just writing or a simple logo design. I am not the most creative person in the world but have put together a more detailed brief listing some of the key information that needs to be included on the pouch (See attachment) Please feel free if you have experience of this the sports supplement market or have different ideas then please feel free to explore them.
The pouch would either be printed straight onto the pouch, or possibly just a printed label (front & back) to be stuck onto the pouch. Please design either or both.
Open to different colour schemes. Design has to be modern looking and eye-catching.
Some key points;
High quality whey protein concentrate
All Natural
Soy free
Great tasting
Please google image search 'protein pouches' to see other designs if your not familiar with the sports supplement market.
Any questions feel free to ask.
Updates
Hi, Thanks for all your design! I am really busy at the moment so haven't had chance to give feedback and have a proper look through all the designs. I have extended the time frame to give myself chance to give proper feedback and see any changes needed. Expect feedback sunday at the latest, and I will be pick a design early next week.
Target Market(s)
Sports supplement market. Product is a whey protein shake
Industry/Entity Type
Nutrition
Look and feel
Each slider illustrates characteristics of the customer's brand and the style your logo design should communicate.

```html
<!DOCTYPE html>
<html lang="en">
<head>
<meta charset="utf-8">
<title>Stellar Fuelworks – Natural Whey Protein Pouch</title>
<link rel="stylesheet" href="https://fonts.googleapis.com/css2?family=Montserrat:wght@400;600;700;800&family=Quicksand:wght@300;400;500;600;700&display=swap">
<style>
  :root{
    --bg:#e4e5e6;
    --silver-light:#eeeff0;
    --silver:#cfd1d3;
    --blue:#1f87d8;
    --blue-deep:#1466ad;
    --white:#ffffff;
    --ink:#2d3a48;
    --red:#d5412c;
    --red-dark:#b02e1c;
    --green:#2f9a44;
    --green-dark:#1d6a2b;
    --head:"Montserrat", sans-serif;
    --body:"Quicksand", sans-serif;
  }
  *{box-sizing:border-box;margin:0;padding:0}
  html,body{width:1200px;height:900px;overflow:hidden}
  body{background:var(--bg);font-family:var(--body);position:relative}

  .pouch{
    position:absolute;top:58px;width:540px;height:790px;
    background:linear-gradient(160deg,var(--silver-light) 0%,var(--silver) 55%,var(--silver-light) 100%);
    border-radius:6px;overflow:hidden;
  }
  .pouch--front{left:38px}
  .pouch--back{left:622px}

  .tear-strip{
    position:absolute;top:10px;left:0;right:0;height:24px;background:var(--blue);
    color:var(--white);font:500 17px/24px var(--body);text-align:right;padding-right:36px;
  }
  .tear-strip::before{
    content:"";position:absolute;left:10px;right:10px;top:11px;border-top:2px dashed rgba(255,255,255,.85);
  }
  .tear-strip span{position:relative;background:var(--blue);padding:0 10px}
  .tear-strip::after{
    content:"";position:absolute;right:16px;top:5px;border-left:13px solid var(--white);
    border-top:7px solid transparent;border-bottom:7px solid transparent;
  }

  /* front */
  .brand{
    position:absolute;top:120px;left:0;right:0;text-align:center;
    font:800 44px/1 var(--head);color:var(--blue);letter-spacing:-.5px;
  }
  .product-name{
    position:absolute;top:174px;left:0;right:0;text-align:center;
    font:300 35px/1 var(--body);color:var(--blue);letter-spacing:.5px;
  }
  .flavour-art{
    position:absolute;left:160px;top:395px;width:380px;height:327px;
    background:linear-gradient(200deg,var(--green-dark) 0%,var(--red) 28%,var(--red-dark) 100%);
  }
  .connectors{position:absolute;inset:0;width:540px;height:790px}
  .hex{
    position:absolute;display:flex;align-items:center;justify-content:center;text-align:center;
    clip-path:polygon(50% 0,100% 25%,100% 75%,50% 100%,0 75%,0 25%);
    background:var(--blue);color:var(--white);font-family:var(--head);font-weight:700;line-height:1.2;
  }
  .hex--no-artificial{left:47px;top:218px;width:200px;height:172px;font-size:22px}
  .hex--protein{left:322px;top:230px;width:165px;height:178px;font-size:19px}
  .hex--amino{left:176px;top:355px;width:180px;height:198px;font-size:20px;background:var(--blue-deep)}
  .hex--soy{left:68px;top:505px;width:140px;height:152px;font-size:31px;line-height:1.05}
  .hex--flavour{left:320px;top:555px;width:96px;height:126px;font-size:11px}
  .servings{
    position:absolute;top:690px;right:70px;font:700 17px/1 var(--head);color:var(--white);
  }
  .social-band{
    position:absolute;left:0;right:0;bottom:0;height:68px;background:var(--blue);
    display:flex;align-items:center;justify-content:center;gap:18px;
    font:600 15px/1 var(--body);color:var(--white);
  }

  /* back */
  .intro{
    position:absolute;top:174px;left:0;right:0;height:140px;background:var(--blue);
    padding:12px 34px;color:var(--white);font:400 16.5px/1.2 var(--body);text-align:center;
  }
  .nutrition{
    position:absolute;left:22px;top:330px;width:226px;height:312px;background:var(--blue);
    color:var(--white);padding:8px 8px;font:400 9.3px/1.16 var(--body);
  }
  .nutrition h2{font:800 21px/1 var(--head);margin-bottom:2px}
  .nutrition .rule{border-top:3px solid var(--white);margin:3px 0}
  .nutrition .thin{border-top:1px solid rgba(255,255,255,.7);margin:2px 0}
  .nutrition .row{display:flex;justify-content:space-between;border-bottom:1px solid rgba(255,255,255,.35)}
  .nutrition .row.sub{padding-left:4px}
  .nutrition .note{margin-top:5px}
  .natural-art{
    position:absolute;left:252px;top:318px;width:262px;height:88px;
    background:linear-gradient(160deg,var(--green) 0%,var(--green-dark) 100%);
    border-radius:4px;
  }
  .natural-title{
    position:absolute;left:266px;top:338px;font:600 24px/1.05 var(--body);color:var(--white);
  }
  .feature{position:absolute;left:255px;width:285px;height:80px}
  .feature--build{top:420px}
  .feature--amino{top:500px}
  .feature--natural{top:580px}
  .feature-band{
    position:absolute;left:45px;right:0;top:10px;height:56px;background:var(--blue);
    color:var(--white);font:500 17px/1.12 var(--body);padding:7px 0 0 50px;
  }
  .feature-icon{
    position:absolute;left:0;top:0;width:70px;height:78px;
    clip-path:polygon(50% 0,100% 25%,100% 75%,50% 100%,0 75%,0 25%);
    background:var(--blue-deep);display:flex;align-items:center;justify-content:center;
  }
  .feature-icon .icon-art{width:40px;height:40px;background:rgba(255,255,255,.85);border-radius:50% 50% 20% 20%}
  .disclaimer{
    position:absolute;top:654px;left:40px;right:40px;text-align:center;
    font:400 11px/1.15 var(--body);color:var(--ink);
  }
  .back-footer{
    position:absolute;left:0;right:0;bottom:0;height:92px;background:var(--blue);
    color:var(--white);text-align:center;font:400 11px/1.3 var(--body);padding-top:24px;
  }
  .back-footer p+p{margin-top:12px}
</style>
</head>
<body>

<section class="pouch pouch--front" aria-label="Front of pouch">
  <div class="tear-strip"><span>Tear here &amp; Reseal For Freshness</span></div>
  <h1 class="brand">STELLAR FUELWORKS</h1>
  <p class="product-name">NATURAL WHEY PROTEIN</p>

  <div class="flavour-art" role="img" aria-label="Illustration of a large strawberry with green leaves"></div>

  <svg class="connectors" viewBox="0 0 540 790" aria-hidden="true">
    <g stroke="#1f87d8" stroke-width="9">
      <line x1="180" y1="375" x2="215" y2="405"/>
      <line x1="350" y1="385" x2="372" y2="355"/>
      <line x1="200" y1="530" x2="180" y2="548"/>
      <line x1="318" y1="520" x2="345" y2="565"/>
    </g>
  </svg>

  <div class="hex hex--no-artificial">NO<br>ARTIFICIAL<br>FLAVOURS</div>
  <div class="hex hex--protein">80% HIGH<br>QUALITY<br>PROTEIN<br>CONTENT</div>
  <div class="hex hex--amino">EXCELLENT<br>AMINO ACID<br>PROFILE</div>
  <div class="hex hex--soy">SOY<br>FREE</div>
  <div class="hex hex--flavour">NEW<br>STRAWBERRY<br>FLAVOUR</div>

  <p class="servings">909G - 30 SERVINGS</p>

  <footer class="social-band">
    <span>Chatterly</span><span>Friendhub</span><span>Pluscircle</span><span>Vidreel</span><span>Photolane</span>
  </footer>
</section>

<section class="pouch pouch--back" aria-label="Back of pouch">
  <div class="tear-strip"><span>Tear here &amp; Reseal For Freshness</span></div>

  <p class="intro">Stellar Fuelworks’ natural whey protein is a very high quality 100% natural instant whey protein concentrate impressively providing 80% protein content making this the perfect supplement to aid muscular growth and repair. In addition this all the ingredients are natural but yet still providing a great taste which will make you want more.</p>

  <div class="nutrition">
    <h2>NUTRITION FACTS</h2>
    <div>Serving Size: 4fl. oz. (120ml)</div>
    <div>Servings Per Bottle: 1</div>
    <div class="rule"></div>
    <div>Amount Per Serving</div>
    <div class="row"><span>Calories: 130</span><span>Calories from fat: 0</span></div>
    <div class="row" style="justify-content:flex-end"><span>% Daily Value*</span></div>
    <div class="row"><span>Total Fat 0g</span><span>0%</span></div>
    <div class="row sub"><span>– Saturated Fat 0g</span><span>0%</span></div>
    <div class="row sub"><span>– Trans Fat 0g</span><span>0%</span></div>
    <div class="row"><span>Cholesterol 0mg</span><span>0%</span></div>
    <div class="row"><span>Sodium 90mg</span><span>4%</span></div>
    <div class="row"><span>Potassium 120mg</span><span>4%</span></div>
    <div class="row"><span>Total Carbohydrate 0g</span><span>0%</span></div>
    <div class="row sub"><span>– Dietry Fiber 0g</span><span>0%</span></div>
    <div class="row sub"><span>– Sugars 0g</span><span>0%</span></div>
    <div class="row"><span>Protein 32g</span><span>64%</span></div>
    <div class="thin"></div>
    <div class="row"><span>Vitamin A &nbsp;&nbsp;0%</span><span>Vitamin C &nbsp;&nbsp;0%</span></div>
    <div class="row"><span>Calcium &nbsp;&nbsp;&nbsp;&nbsp;0%</span><span>Iron &nbsp;&nbsp;&nbsp;&nbsp;9%</span></div>
    <p class="note">*Percent Daily Values are based on a 2,000 calorie diet. Your daily values may be higher or lower depending on your caloric needs.</p>
  </div>

  <div class="natural-art" role="img" aria-label="Large green leaf behind the heading"></div>
  <h2 class="natural-title">ALL NATURAL<br>INGREDIENTS</h2>

  <div class="feature feature--build">
    <div class="feature-band">Build, repair<br>and grow</div>
    <div class="feature-icon"><div class="icon-art" role="img" aria-label="Flexed arm muscle icon"></div></div>
  </div>
  <div class="feature feature--amino">
    <div class="feature-band">Excellent Amino<br>Acid profile</div>
    <div class="feature-icon">
      <svg width="54" height="40" viewBox="0 0 54 40" aria-hidden="true" fill="none" stroke="#fff" stroke-width="2.5">
        <polygon points="10,14 18,18 18,27 10,31 2,27 2,18"/>
        <polygon points="27,9 35,13 35,22 27,26 19,22 19,13"/>
        <polygon points="44,14 52,18 52,27 44,31 36,27 36,18"/>
      </svg>
    </div>
  </div>
  <div class="feature feature--natural">
    <div class="feature-band">No artificial<br>Flavours</div>
    <div class="feature-icon">
      <svg width="40" height="40" viewBox="0 0 40 40" aria-hidden="true" fill="none" stroke="#fff" stroke-width="4">
        <circle cx="20" cy="20" r="16"/><line x1="9" y1="31" x2="31" y2="9"/>
      </svg>
    </div>
  </div>

  <p class="disclaimer">Do not exceed serving suggestion, and always consult a doctor before use. Natural whey protein should be consumed alongside a well balanced healthy diet and training programme.</p>

  <footer class="back-footer">
    <p>For any enquiries visit our website – www.</p>
    <p>UK manufactured. Stellar Fuelworks, unit 7, Orbit Court, Larkfield, LK4 2QR, UK</p>
  </footer>
</section>

</body>
</html>
```